Interior Design & Furniture E commerce Website Design

I need a cutting edge website design, this is for Interior Design Services as well as eCommerce for furniture and home decor www.lorivellstudio.com
Here is a sample of the concept behind the site.
I am a furniture & Interior Designer, want to create a life style brand.
Will offer Interior Design Services : Commercial & Residential (this portion will be a catalog or portfolio type)
The eCommerce side will sell, Furniture, Lighting, Decor, Gifts, Textiles, will also be offering trade so that could be at bottom of site. I also like the concept of concierge as where all the info falls under: shipping, etc..

*Please make sure to make the eCommerce prominent.

Hello Designers, I also would like to possibly update my logo, the current one I like but don't Love.

Target Market(s)

High end customers with disposable income, who also appreciate quality and unique furniture & design

Number of Pages Required

5+ page

Colors
0255a3
f37122

Requirements
Must have
• Room Planer: I will be using this tool http://kvstudio.tarnebworks.com/room-planner.inc
• Live Chat
• Will be offering 3d renderings for spaces as well as Virtual Reality
• The image I loaded that looks like copper, I would like to have that as a color on the site with the texture: so the colors are Blue and copper. Would like the site to be user friendly and interactive
• http://kvstudio.tarnebworks.com/ (this is the current site in development, so we will be offering Design your own, Trends, inspiration, etc...
• I have included a headshot to use for now about me. or about us.
• I also included several actual project installation (residential and commercial) as well as a variety of my furniture items
• I have Included an old Bio and some articles I would like to show case in a Press Area
• I would also like to include a section for Events (Giving back )I do a lot of charity events 1-2 a year and would like to showcase that as well
• *Please make the store (ecommerce prominent )

```html
<!DOCTYPE html>
<html lang="en">
<head>
<meta charset="utf-8">
<title>Lori Vell Studio — Home</title>
<link href="https://fonts.googleapis.com/css2?family=Open+Sans:ital,wght@0,300;0,400;0,600;0,700;1,400&display=swap" rel="stylesheet">
<style>
:root{
  --page:#f6f4f4;
  --white:#ffffff;
  --ink:#3a3f47;
  --ink-soft:#555a61;
  --copper:#b3663d;
  --hero-top:#f4f4f4;
  --hero-bottom:#e6e6e6;
  --sofa:#2d4396;
  --sofa-dark:#1a2766;
  --chaise:#a9bfe6;
}
*{margin:0;padding:0;box-sizing:border-box}
html,body{width:1200px;height:1191px;overflow:hidden}
body{background:var(--page);font-family:"Open Sans",sans-serif;color:var(--ink);position:relative}
.abs{position:absolute}
.view-label{position:absolute;top:26px;font-size:15px;letter-spacing:.5px;color:var(--ink-soft);transform:translateX(-50%)}
.frame{position:absolute;top:74px;bottom:0;background:var(--white);box-shadow:0 0 10px rgba(0,0,0,.08);overflow:hidden}
.desktop{left:83px;width:636px}
.mobile{left:766px;width:348px}
.hero{position:absolute;left:0;right:0;background:linear-gradient(180deg,var(--hero-top),var(--hero-bottom))}
.brand{position:absolute;display:flex;align-items:center;gap:6px;color:var(--copper);font-weight:400;letter-spacing:1.5px;white-space:nowrap}
.brand .mark{width:10px;height:10px;border:1.2px solid var(--copper);border-radius:50%}
.util{position:absolute;font-size:9px;color:var(--ink);white-space:nowrap}
.icon{position:absolute}
.badge{position:absolute;width:5px;height:5px;border-radius:50%;background:var(--copper)}
.nav span{position:absolute;top:59px;white-space:nowrap;font-size:8.8px;font-weight:600;color:var(--ink)}
.btn-outline{position:absolute;border:1px solid var(--ink);font-size:8px;font-weight:600;display:flex;align-items:center;justify-content:center;letter-spacing:.3px;white-space:nowrap}
.btn-copper{border-color:var(--copper);color:var(--copper)}
.link-arrow{position:absolute;font-size:8.2px;font-weight:600;letter-spacing:.3px;white-space:nowrap}
.since{position:absolute;font-size:8px;color:var(--copper);letter-spacing:.3px}
.kicker{position:absolute;font-weight:300;color:var(--ink);white-space:nowrap}
.headline{position:absolute;font-weight:600;color:var(--ink);white-space:nowrap}
.rule{position:absolute;height:2px;background:var(--ink)}
.lede{position:absolute;font-size:10px;line-height:14px;color:var(--ink-soft)}
.dots{position:absolute;display:flex;gap:6px}
.dots i{width:7px;height:7px;border-radius:50%;border:1.2px solid var(--ink);display:block}
.dots i.on{background:var(--ink)}
.photo{position:absolute}
.section-title{position:absolute;font-weight:300;color:var(--ink);white-space:nowrap}
.section-title b{font-weight:600}
.body-copy{position:absolute;font-size:10px;line-height:14px;color:var(--ink-soft)}
.body-copy p+p{margin-top:9px}
.play{display:inline-block;width:9px;height:9px;border-radius:50%;background:var(--ink);vertical-align:-1px;margin-right:9px;position:relative}
.play:after{content:"";position:absolute;left:3.5px;top:2.3px;border-left:3.5px solid #fff;border-top:2.2px solid transparent;border-bottom:2.2px solid transparent}
.tile{position:absolute;overflow:hidden;color:var(--white);text-align:center}
.tile-photo{position:absolute;inset:0}
.tile-photo:after{content:"";position:absolute;inset:0;background:radial-gradient(ellipse at 50% 50%,rgba(40,40,40,.35),rgba(40,40,40,0) 70%)}
.tile-body{position:absolute;left:0;right:0;display:flex;flex-direction:column;align-items:center;padding:0 10px}
.tile-title{font-weight:600;letter-spacing:.3px;text-shadow:0 1px 3px rgba(0,0,0,.45);white-space:nowrap}
.tile-rule{width:18px;height:2px;background:var(--white);margin:4px 0 6px}
.tile-text{font-size:8px;line-height:12px;text-shadow:0 1px 2px rgba(0,0,0,.5)}
.tile-btn{margin-top:6px;border:1px solid var(--white);font-size:6px;font-weight:600;padding:3px 8px;letter-spacing:.3px;white-space:nowrap;background:rgba(0,0,0,.12)}
.studio{background:radial-gradient(ellipse at 85% 20%,#6f7a5e 0%,rgba(111,122,94,0) 35%),radial-gradient(ellipse at 12% 85%,#5f6b4f 0%,rgba(95,107,79,0) 30%),radial-gradient(ellipse at 50% 90%,#6b5a48 0%,rgba(107,90,72,0) 35%),linear-gradient(135deg,#a8a8a4,#8a8a86 50%,#6c6c69)}
.plan{background:radial-gradient(ellipse at 40% 75%,#d9d2cb 0%,rgba(217,210,203,0) 35%),radial-gradient(ellipse at 20% 15%,#c9c9c9 0%,rgba(201,201,201,0) 40%),linear-gradient(135deg,#bdbdbd,#9b9b9b 55%,#b3b3b3)}
.vr{background:radial-gradient(ellipse at 55% 25%,#2b2b2b 0%,rgba(43,43,43,0) 35%),radial-gradient(ellipse at 45% 80%,#c4c4c4 0%,rgba(196,196,196,0) 40%),linear-gradient(160deg,#9a9a9a,#6e6e6e 55%,#8a8a8a)}
.ideas{background:radial-gradient(ellipse at 20% 50%,#6a5d55 0%,rgba(106,93,85,0) 35%),radial-gradient(ellipse at 80% 45%,#8c7f74 0%,rgba(140,127,116,0) 35%),radial-gradient(ellipse at 50% 10%,#9aa08c 0%,rgba(154,160,140,0) 40%),linear-gradient(135deg,#7d7d7d,#5c5c5c 50%,#8a8a8a)}
.hamburger{position:absolute;left:11px;top:12px;width:25px;height:25px;border-radius:50%;border:1px solid #d8d8d8;display:flex;flex-direction:column;justify-content:center;align-items:center;gap:2.5px}
.hamburger i{display:block;width:11px;height:1.6px;background:var(--copper)}
.mobile-header{position:absolute;left:0;right:0;top:0;height:45px;background:var(--white);box-shadow:0 1px 4px rgba(0,0,0,.06);z-index:2}
</style>
</head>
<body>

<div class="view-label" style="left:401px">DESKTOP VIEW</div>
<div class="view-label" style="left:940px">MOBILE VIEW</div>

<section class="frame desktop">
  <div class="hero" style="top:0;height:344px"></div>

  <div class="brand" style="left:62px;top:36px;font-size:14px"><span class="mark"></span>LORI VELL</div>

  <div class="util" style="left:419px;top:23px">Login / Register</div>
  <svg class="icon" style="left:500px;top:21px" width="16" height="14" viewBox="0 0 16 14"><path d="M8 13S1 8.5 1 4.5A3.4 3.4 0 0 1 8 3a3.4 3.4 0 0 1 7 1.5C15 8.5 8 13 8 13z" fill="none" stroke="#3a3f47" stroke-width="1.2"/></svg>
  <span class="badge" style="left:512px;top:19px"></span>
  <svg class="icon" style="left:530px;top:18px" width="14" height="16" viewBox="0 0 14 16"><rect x="1" y="5" width="12" height="10" fill="none" stroke="#3a3f47" stroke-width="1.2"/><path d="M4 5V3.5a3 3 0 0 1 6 0V5" fill="none" stroke="#3a3f47" stroke-width="1.2"/></svg>
  <span class="badge" style="left:541px;top:16px"></span>
  <div class="abs" style="left:556px;top:21px;width:1px;height:12px;background:#3a3f47"></div>
  <svg class="icon" style="left:566px;top:23px" width="10" height="10" viewBox="0 0 10 10"><circle cx="4" cy="4" r="3" fill="none" stroke="#3a3f47" stroke-width="1.2"/><path d="M6.3 6.3L9 9" stroke="#3a3f47" stroke-width="1.2"/></svg>

  <nav class="nav">
    <span style="left:223px">HOME</span>
    <span style="left:267px">ABOUT</span>
    <span style="left:315px">DESIGN SERVICES</span>
    <span style="left:405px">MY SHOP</span>
    <span style="left:462px">BLOG</span>
  </nav>
  <div class="btn-outline" style="left:508px;top:49px;width:66px;height:20px;border-width:1.4px">CONTACT</div>

  <div class="photo" role="img" aria-label="Navy blue upholstered sectional sofa with patterned cushions" style="left:258px;top:112px;width:374px;height:176px;background:radial-gradient(ellipse at 42% 30%,#d9d9d6 0%,rgba(217,217,214,0) 14%),radial-gradient(ellipse at 58% 28%,#cfcfcc 0%,rgba(207,207,204,0) 13%),radial-gradient(ellipse 48% 40% at 52% 56%,var(--sofa) 0%,var(--sofa) 55%,var(--sofa-dark) 78%,rgba(230,230,230,0) 100%)"></div>

  <div class="since" style="left:61px;top:116px">SINCE 1979</div>
  <div class="kicker" style="left:61px;top:130px;font-size:21px">WHEN FURNITURE</div>
  <div class="headline" style="left:60px;top:155px;font-size:27px">COMES TO LIFE</div>
  <div class="rule" style="left:61px;top:195px;width:28px"></div>
  <div class="lede" style="left:61px;top:215px;width:205px">I am a furniture &amp; Interior Designer, want to create a life style brand.</div>
  <div class="btn-outline" style="left:62px;top:260px;width:83px;height:22px">GET STARTED</div>
  <div class="link-arrow" style="left:161px;top:266px">SHOP NOW &nbsp;›</div>
  <div class="dots" style="left:303px;top:302px"><i class="on"></i><i></i><i></i></div>

  <div class="photo" role="img" aria-label="Black and white portrait of the designer" style="left:0;top:346px;width:267px;height:310px;background:radial-gradient(ellipse 22% 26% at 52% 38%,#cfcfcf 0%,#bdbdbd 60%,rgba(80,80,80,0) 100%),radial-gradient(ellipse 42% 48% at 48% 40%,#4e4e4e 0%,#6d6d6d 55%,rgba(120,120,120,0) 100%),radial-gradient(ellipse 60% 45% at 45% 90%,#b8b8b8 0%,rgba(200,200,200,0) 100%),linear-gradient(90deg,#e6e6e6,#ffffff 95%)"></div>

  <div class="section-title" style="left:326px;top:396px;font-size:21px">ABOUT <b>LORI VELL</b></div>
  <div class="rule" style="left:326px;top:431px;width:28px"></div>
  <div class="body-copy" style="left:326px;top:451px;width:246px">
    <p>&nbsp;As a child, Lori Vell-Hartwick would spend quality time with her Father by helping out in his <i>furniture manufacturing company</i>. She was delighted to be taken along on project installations to exciting places like the Marquesa in Las Vegas.</p>
    <p>What began as a fun after-school activity evolved into a passion for quality craftsmanship and unique furniture &amp; interior/exterior space design.</p>
  </div>
  <div class="btn-outline btn-copper" style="left:326px;top:586px;width:82px;height:24px;border-width:1.4px">LEARN MORE</div>
  <div class="link-arrow" style="left:427px;top:593px"><span class="play"></span>WATCH MY VIDEO</div>

  <div class="tile" style="left:62px;top:676px;width:316px;height:176px">
    <div class="tile-photo studio" role="img" aria-label="Bright studio interior with plants and shelving"></div>
    <div class="tile-body" style="top:44px">
      <div class="tile-title" style="font-size:15px">BUILD YOUR CUSTOM FURNITURE</div>
      <div class="tile-rule"></div>
      <div class="tile-text" style="width:260px">When browsing specific brands on our website you will have the option of customizing such items as sofas, chairs, loveseats, sectionals and so much more.</div>
      <div class="tile-btn">BROWSE CUSTOM FORNITURE</div>
    </div>
  </div>
  <div class="tile" style="left:392px;top:676px;width:182px;height:176px">
    <div class="tile-photo plan" role="img" aria-label="Hands sketching a floor plan on a drafting table"></div>
    <div class="tile-body" style="top:55px">
      <div class="tile-title" style="font-size:15px">ROOM PLANNER</div>
      <div class="tile-rule"></div>
      <div class="tile-text">Design Your Perfect Space</div>
      <div class="tile-btn">GET STARTED</div>
    </div>
  </div>
  <div class="tile" style="left:62px;top:862px;width:182px;height:176px">
    <div class="tile-photo vr" role="img" aria-label="Person wearing a virtual reality headset"></div>
    <div class="tile-body" style="top:54px">
      <div class="tile-title" style="font-size:15px">VR SERVICE</div>
      <div class="tile-rule"></div>
      <div class="tile-text">We offer 3D renderings for spaces</div>
      <div class="tile-btn">LEARN MORE</div>
    </div>
  </div>
  <div class="tile" style="left:258px;top:862px;width:316px;height:176px">
    <div class="tile-photo ideas" role="img" aria-label="Two people discussing ideas at a laptop"></div>
    <div class="tile-body" style="top:42px">
      <div class="tile-title" style="font-size:15px">IDEAS &amp; INSPIRATION</div>
      <div class="tile-rule"></div>
      <div class="tile-text" style="width:250px">Lorem ipsum dolor sit amet, consectetur adipiscing elit. Fusce id placerat mi, auctor aliquam elit. Cras finibus nulla enim, non scelerisque justo tempus at.</div>
      <div class="tile-btn">GET INSPIRED</div>
    </div>
  </div>

  <div class="section-title" style="left:61px;top:1095px;font-size:20px">MY DESIGN <b>SERVICES</b></div>
  <div class="photo" role="img" aria-label="Warm wooden interior detail" style="left:324px;top:1097px;width:250px;height:30px;background:linear-gradient(90deg,#b89266,#e2cba4 60%,#d4b78c)"></div>
</section>

<section class="frame mobile">
  <header class="mobile-header">
    <div class="hamburger"><i></i><i></i><i></i></div>
    <div class="brand" style="left:128px;top:16px;font-size:11px"><span class="mark" style="width:8px;height:8px"></span>LORI VELL</div>
    <svg class="icon" style="left:288px;top:16px" width="16" height="14" viewBox="0 0 16 14"><path d="M8 13S1 8.5 1 4.5A3.4 3.4 0 0 1 8 3a3.4 3.4 0 0 1 7 1.5C15 8.5 8 13 8 13z" fill="none" stroke="#3a3f47" stroke-width="1.2"/></svg>
    <span class="badge" style="left:300px;top:14px"></span>
    <svg class="icon" style="left:320px;top:14px" width="14" height="16" viewBox="0 0 14 16"><rect x="1" y="5" width="12" height="10" fill="none" stroke="#3a3f47" stroke-width="1.2"/><path d="M4 5V3.5a3 3 0 0 1 6 0V5" fill="none" stroke="#3a3f47" stroke-width="1.2"/></svg>
    <span class="badge" style="left:331px;top:12px"></span>
  </header>

  <div class="hero" style="top:45px;height:281px"></div>
  <div class="photo" role="img" aria-label="Light blue tufted chaise lounge on wooden legs" style="left:44px;top:110px;width:256px;height:190px;background:radial-gradient(ellipse 40% 12% at 50% 92%,rgba(120,110,100,.35) 0%,rgba(120,110,100,0) 100%),radial-gradient(ellipse 46% 26% at 50% 55%,#c7d6ef 0%,var(--chaise) 55%,#8ea7d4 78%,rgba(230,230,230,0) 100%),radial-gradient(ellipse 18% 30% at 86% 30%,#b8cbeb 0%,rgba(184,203,235,0) 100%)"></div>
  <div class="since" style="left:0;right:0;text-align:center;top:80px">SINCE 1979</div>
  <div class="kicker" style="left:0;right:0;text-align:center;top:98px;font-size:16px">WHEN FURNITURE</div>
  <div class="headline" style="left:0;right:0;text-align:center;top:117px;font-size:26px">COMES TO LIFE</div>
  <div class="rule" style="left:160px;top:155px;width:28px"></div>
  <div class="lede" style="left:78px;top:180px;width:192px;text-align:center">I am a furniture &amp; Interior Designer, want to create a life style brand.</div>
  <div class="btn-outline" style="left:97px;top:224px;width:83px;height:22px">GET STARTED</div>
  <div class="link-arrow" style="left:196px;top:230px">SHOP NOW &nbsp;›</div>
  <div class="dots" style="left:154px;top:268px"><i class="on"></i><i></i><i></i></div>

  <div class="section-title" style="left:0;right:0;text-align:center;top:362px;font-size:20px">ABOUT <b>LORI VELL</b></div>
  <div class="rule" style="left:160px;top:396px;width:28px"></div>
  <div class="body-copy" style="left:52px;top:416px;width:244px;text-align:center;font-size:10.8px;line-height:15px">
    <p>As a child, Lori Vell-Hartwick would spend quality time with her Father by helping out in his <i>furniture manufacturing company</i>. She was delighted to be taken along on project installations to exciting places like the Marquesa in Las Vegas.</p>
    <p>What began as a fun after-school activity evolved into a passion for quality craftsmanship and unique furniture &amp; interior/exterior space design.</p>
  </div>
  <div class="btn-outline" style="left:80px;top:576px;width:81px;height:24px;border-width:1.4px">LEARN MORE</div>
  <div class="link-arrow" style="left:180px;top:583px"><span class="play"></span>WATCH MY VIDEO</div>

  <div class="tile" style="left:12px;top:642px;width:325px;height:158px">
    <div class="tile-photo studio" role="img" aria-label="Bright studio interior with plants and shelving"></div>
    <div class="tile-body" style="top:40px">
      <div class="tile-title" style="font-size:15px">BUILD YOUR CUSTOM FURNITURE</div>
      <div class="tile-rule"></div>
      <div class="tile-text" style="width:260px">When browsing specific brands on our website you will have the option of customizing such items as sofas, chairs, loveseats, sectionals and so much more.</div>
      <div class="tile-btn">BROWSE CUSTOM FORNITURE</div>
    </div>
  </div>
  <div class="tile" style="left:12px;top:808px;width:159px;height:158px">
    <div class="tile-photo plan" role="img" aria-label="Hands sketching a floor plan on a drafting table"></div>
    <div class="tile-body" style="top:53px">
      <div class="tile-title" style="font-size:14px">ROOM PLANNER</div>
      <div class="tile-rule"></div>
      <div class="tile-text">Design Your Perfect Space</div>
      <div class="tile-btn">GET STARTED</div>
    </div>
  </div>
  <div class="tile" style="left:177px;top:808px;width:160px;height:158px">
    <div class="tile-photo vr" role="img" aria-label="Person wearing a virtual reality headset"></div>
    <div class="tile-body" style="top:53px">
      <div class="tile-title" style="font-size:14px">VR SERVICE</div>
      <div class="tile-rule"></div>
      <div class="tile-text">We offer 3D renderings for spaces</div>
      <div class="tile-btn">LEARN MORE</div>
    </div>
  </div>
  <div class="tile" style="left:12px;top:974px;width:325px;height:160px">
    <div class="tile-photo ideas" role="img" aria-label="Two people discussing ideas at a laptop"></div>
    <div class="tile-body" style="top:36px">
      <div class="tile-title" style="font-size:15px">IDEAS &amp; INSPIRATION</div>
      <div class="tile-rule"></div>
      <div class="tile-text" style="width:250px">Lorem ipsum dolor sit amet, consectetur adipiscing elit. Fusce id placerat mi, auctor aliquam elit. Cras finibus nulla enim, non scelerisque justo tempus at.</div>
      <div class="tile-btn">GET INSPIRED</div>
    </div>
  </div>
</section>

</body>
</html>
```